Thistle Root Organic

Please find attached screenshots of a same product as what I'm selling, looking for similar packaging but yet a whole new different design with my own logo rivertiles which is also attached. It will be on white bags with the clear on the bottom center. As far as colors maby green yellow and black or if you have a better idea. Also it needs to be something that looks up to date modern I like when it has that two-tone gloss to it where it goes from darker to lighter.

```html
<!DOCTYPE html>
<html lang="en">
<head>
<meta charset="utf-8">
<title>Thistle Root Organic – Pouch Front</title>
<link rel="stylesheet" href="https://fonts.googleapis.com/css2?family=Alfa+Slab+One&family=Montserrat:wght@500;600;700&family=Open+Sans:wght@700&display=swap">
<style>
  :root {
    --backdrop: #166341;
    --pouch-dark: #151515;
    --pouch-mid: #242424;
    --brand-green: #1a6a42;
    --title-green: #1a9c5c;
    --title-green-light: #22a866;
    --leaf-yellow: #e1bd1f;
    --organic-red: #d63d1f;
    --organic-orange: #f2651c;
    --band-green: #1fa35a;
    --band-yellow: #f5d21e;
    --ink: #1b1b1b;
    --white: #ffffff;
  }
  * { box-sizing: border-box; margin: 0; padding: 0; }
  html, body { width: 1200px; height: 960px; overflow: hidden; }
  body { background: var(--backdrop); position: relative; font-family: "Montserrat", sans-serif; }

  .pouch {
    position: absolute; left: 340px; top: 68px; width: 520px; height: 781px;
    border-radius: 26px 26px 8px 8px; overflow: hidden;
    background: linear-gradient(100deg, var(--pouch-dark) 0%, var(--pouch-mid) 50%, var(--pouch-dark) 100%);
  }
  .brand-tab {
    position: absolute; left: 135px; top: 0; width: 250px; height: 295px;
    background: linear-gradient(180deg, #1d7048 0%, var(--brand-green) 100%);
  }
  .hang-hole {
    position: absolute; left: 79px; top: 55px; width: 92px; height: 14px;
    border: 1.5px solid rgba(255,255,255,0.18); border-radius: 7px;
  }
  .brand-mark {
    position: absolute; left: 50%; top: 127px; width: 96px; height: 96px;
    transform: translateX(-50%); border: 5px solid var(--white); border-radius: 50%;
  }
  .brand-name {
    position: absolute; left: 0; right: 0; top: 234px; text-align: center;
    color: var(--white); font-weight: 600; font-size: 27px; letter-spacing: 2px;
  }

  .product-title {
    position: absolute; left: 0; right: 0; top: 340px; text-align: center;
    font-family: "Alfa Slab One", serif; font-size: 60px; line-height: 1;
    color: var(--title-green); letter-spacing: 1px;
  }
  .product-part {
    position: absolute; left: 85px; right: 85px; top: 404px;
    display: flex; align-items: center; gap: 12px;
    color: var(--leaf-yellow); font-weight: 600; font-size: 25px; letter-spacing: 2px;
  }
  .product-part::before, .product-part::after {
    content: ""; flex: 1; height: 4px; background: var(--leaf-yellow);
  }
  .product-grade {
    position: absolute; left: 0; right: 0; top: 425px; text-align: center;
    font-weight: 500; font-size: 50px; letter-spacing: 4px; line-height: 1.1;
    background: linear-gradient(90deg, var(--organic-red), var(--organic-orange));
    -webkit-background-clip: text; background-clip: text; color: transparent;
  }

  .herb-photo {
    position: absolute; left: 62px; top: 521px; width: 396px; height: 200px;
    border-radius: 198px 198px 0 0;
    background: radial-gradient(ellipse at 50% 40%, #7d7a4c 0%, #5e6638 55%, #3f5a2c 100%);
  }

  .weight-band {
    position: absolute; left: 0; right: 0; top: 713px; height: 42px;
    background: linear-gradient(90deg, #169a50, var(--band-green) 60%, #28b06a);
    display: flex; align-items: center; justify-content: center;
    font-family: "Open Sans", sans-serif; font-weight: 700; font-size: 19px; color: var(--ink);
  }
  .base-band {
    position: absolute; left: 0; right: 0; top: 755px; bottom: 0;
    background: linear-gradient(180deg, var(--band-yellow), #e7c114);
  }
</style>
</head>
<body>
  <main class="pouch">
    <section class="brand-tab">
      <div class="hang-hole"></div>
      <div class="brand-mark"></div>
      <div class="brand-name">RIVERTILES</div>
    </section>

    <h1 class="product-title">THISTLE</h1>
    <div class="product-part">ROOT</div>
    <div class="product-grade">ORGANIC</div>

    <div class="herb-photo" role="img" aria-label="Mound of dried cut thistle root herb"></div>

    <div class="weight-band">Net Wt.&nbsp; 1.27 OZ (36g)</div>
    <div class="base-band"></div>
  </main>
</body>
</html>
```